Business Card Design for company

We want new business cards. We'd like something different-- yet still highly professional. Our tagline is Providing leadership, delivering success. Stock photos are ok, as long as they are relevant and look upscale.

Target Market(s)

Architecture/Business Management Consulting/Engineering Consulting

Contact Information for Business Card

dark gray background with pops of blue might be good, but you tell me. You're the designers. Rounded corners might be nice, but again, you tell me.

Font styles to use
Serif
Sans Serif

Colors
3276b5
5c5c5c
9d9d9d
fbfbfb

Requirements
Nice to have
• Something different, but still very professional.

```html
<!DOCTYPE html>
<html lang="en">
<head>
<meta charset="utf-8">
<title>Norvell Advisory – Business Card</title>
<link rel="stylesheet" href="https://fonts.googleapis.com/css2?family=Montserrat:wght@600;700&family=Open+Sans:wght@400&display=swap">
<style>
  :root {
    --blue: #266197;
    --slate: #4a4d52;
    --white: #fbfbfb;
    --circle-light: #fdfdfd;
    --circle-shade: #dcdde0;
    --rule: #5a83ad;
    --page: #e9eaec;
  }
  * { box-sizing: border-box; margin: 0; padding: 0; }
  html, body {
    width: 1200px; height: 900px; overflow: hidden;
    background: var(--page);
  }
  .business-card {
    position: absolute; left: 150px; top: 172px;
    width: 900px; height: 556px;
    background: var(--blue);
    overflow: hidden;
    box-shadow: 0 12px 34px rgba(0,0,0,.18);
  }
  .side-band {
    position: absolute; top: 0; right: 0;
    width: 262px; height: 100%;
    background: var(--slate);
  }
  .brand-circle {
    position: absolute; left: 395px; top: 29px;
    width: 486px; height: 486px; border-radius: 50%;
    background: radial-gradient(circle at 40% 35%, var(--circle-light) 0%, #eeeff1 55%, var(--circle-shade) 100%);
    display: flex; flex-direction: column; align-items: center; justify-content: center;
  }
  .brand-name {
    font-family: "Montserrat", sans-serif; font-weight: 700;
    color: var(--slate); font-size: 50px; line-height: 1.15;
    letter-spacing: 2px; text-align: center;
  }
  .holder {
    position: absolute; left: 39px; top: 52px;
    color: var(--white);
  }
  .holder-name {
    font-family: "Montserrat", sans-serif; font-weight: 700;
    font-size: 30px; letter-spacing: .5px; line-height: 1.1;
  }
  .holder-title {
    font-family: "Open Sans", sans-serif; font-size: 25px; line-height: 1.3;
  }
  .contact-list {
    position: absolute; left: 39px; top: 172px;
    list-style: none; color: var(--white);
    font-family: "Open Sans", sans-serif; font-size: 25px; line-height: 33px;
  }
  .contact-list li { display: flex; align-items: center; gap: 6px; }
  .contact-list svg { width: 20px; height: 20px; fill: var(--white); flex: none; }
  .address {
    position: absolute; left: 39px; top: 311px;
    color: var(--white);
    font-family: "Open Sans", sans-serif; font-size: 25px; line-height: 33px;
    font-style: normal;
  }
  .divider {
    position: absolute; left: 36px; top: 403px;
    width: 340px; height: 1px; background: var(--rule);
  }
  .tagline {
    position: absolute; left: 32px; top: 420px;
    color: var(--white);
    font-family: "Montserrat", sans-serif; font-weight: 600;
    font-size: 24px; line-height: 33px;
  }
</style>
</head>
<body>
  <div class="business-card">
    <div class="side-band"></div>
    <div class="brand-circle">
      <div class="brand-name">NORVELL<br>ADVISORY</div>
    </div>

    <div class="holder">
      <h1 class="holder-name">DANIEL MERCER</h1>
      <p class="holder-title">Managing Director</p>
    </div>

    <ul class="contact-list">
      <li>
        <svg viewBox="0 0 24 24" aria-hidden="true"><path d="M3 9c0-3 4-5 9-5s9 2 9 5v2h-5V9H8v2H3zm3 3h12l2 8H4zm6 2a2.5 2.5 0 1 0 0 5 2.5 2.5 0 0 0 0-5z"/></svg>
        012-345 678 900
      </li>
      <li>
        <svg viewBox="0 0 24 24" aria-hidden="true"><path d="M7 2h10a1 1 0 0 1 1 1v18a1 1 0 0 1-1 1H7a1 1 0 0 1-1-1V3a1 1 0 0 1 1-1zm1 3v12h8V5zm4 13.5a1.2 1.2 0 1 0 0 2.4 1.2 1.2 0 0 0 0-2.4z"/></svg>
        012-345 678 900
      </li>
      <li>
        <svg viewBox="0 0 24 24" aria-hidden="true"><path d="M3 6h18v12H3zm2 1.5 7 5.5 7-5.5z"/></svg>
        info@samplemail.com
      </li>
      <li>
        <svg viewBox="0 0 24 24" aria-hidden="true"><path d="M12 3a9 9 0 1 0 0 18 9 9 0 0 0 0-18zm-1 3c-1 1-3 1-3 3s2 1 3 2 0 3 1 4 2 2 2 3c2-1 4-3 4-6-1 0-2 0-3-1s1-3 0-4-2-1-4-1z"/></svg>
        www.yourdomain.com
      </li>
    </ul>

    <address class="address">12345, Address Goes Here<br>Country Name, 123456</address>

    <div class="divider"></div>

    <p class="tagline">PROVIDING LEADERSHIP<br>DELIVERING SUCCESS</p>
  </div>
</body>
</html>
```